VS Business Card

Design new business cards for VELNAstack

Please see attached for the design brief

**** Please note, please feel free to propose a font that works for a professional, technology company ***

Target Market(s)

Technology buyers

Industry/Entity Type

Business

```html
<!DOCTYPE html>
<html lang="en">
<head>
<meta charset="utf-8">
<title>VELNAstack Business Card</title>
<link rel="stylesheet" href="https://fonts.googleapis.com/css2?family=Source+Sans+3:wght@400;600;700&display=swap">
<style>
  :root {
    --page-bg: #e9ebef;
    --card-white: #ffffff;
    --navy: #1f3470;
    --navy-deep: #1a2c63;
    --sky: #6a8fd0;
    --title-blue: #6b86c4;
    --accent-orange: #f5a623;
    --text-light: #ffffff;
    --shadow: rgba(20, 30, 60, 0.18);
  }
  * { box-sizing: border-box; margin: 0; padding: 0; }
  html, body {
    width: 1200px; height: 900px; overflow: hidden;
    background: var(--page-bg);
    font-family: "Source Sans 3", Arial, sans-serif;
  }
  .canvas {
    position: relative; width: 1200px; height: 900px;
  }
  .card {
    position: absolute; left: 260px;
    width: 680px; height: 389px;
    background: var(--card-white);
    box-shadow: 0 8px 24px var(--shadow);
    overflow: hidden;
  }
  .card--front { top: 45px; }
  .card--back { top: 466px; }

  .wordmark {
    display: flex; align-items: center; gap: 14px;
    color: var(--navy);
    font-weight: 600;
    letter-spacing: 0.5px;
    line-height: 1;
  }
  .wordmark__square {
    background: var(--sky);
    flex: none;
  }
  .card--front .wordmark {
    position: absolute; left: 50%; top: 50%;
    transform: translate(-50%, -50%);
    font-size: 72px;
  }
  .card--front .wordmark__square { width: 46px; height: 46px; }

  .card--back .wordmark {
    position: absolute; right: 38px; top: 42px;
    font-size: 44px;
  }
  .card--back .wordmark__square { width: 28px; height: 28px; }

  .holder { position: absolute; left: 40px; top: 40px; }
  .holder__name {
    color: var(--navy); font-weight: 700; font-size: 24px; line-height: 1.1;
  }
  .holder__title {
    color: var(--title-blue); font-size: 13px; margin-top: 2px;
  }

  .card__swoosh { position: absolute; inset: 0; width: 100%; height: 100%; }

  .contact {
    position: absolute; left: 40px; top: 222px;
    list-style: none; color: var(--text-light);
    font-size: 16px; line-height: 24px;
  }
  .contact__item { display: flex; align-items: center; gap: 9px; }
  .contact__icon { width: 14px; height: 14px; flex: none; }
  .address {
    position: absolute; left: 40px; top: 322px;
    color: var(--text-light); font-size: 16px; line-height: 21px;
    font-style: normal;
  }
</style>
</head>
<body>
<main class="canvas">

  <section class="card card--front" aria-label="Card front">
    <div class="wordmark">
      <span class="wordmark__square"></span>
      <span class="wordmark__name">VELNAstack</span>
    </div>
  </section>

  <section class="card card--back" aria-label="Card back">
    <svg class="card__swoosh" viewBox="0 0 680 389" preserveAspectRatio="none" aria-hidden="true">
      <path d="M0,158 C220,128 480,170 680,368 L680,389 L0,389 Z" fill="var(--sky)"/>
      <path d="M0,176 C220,150 470,200 650,389 L0,389 Z" fill="var(--navy-deep)"/>
    </svg>

    <div class="holder">
      <p class="holder__name">Owen Harlow</p>
      <p class="holder__title">Account Manager</p>
    </div>

    <div class="wordmark">
      <span class="wordmark__square"></span>
      <span class="wordmark__name">VELNAstack</span>
    </div>

    <ul class="contact">
      <li class="contact__item">
        <svg class="contact__icon" viewBox="0 0 14 14" aria-label="Mobile"><rect x="3.5" y="0.5" width="7" height="13" rx="1.5" fill="var(--accent-orange)"/><rect x="5" y="2.5" width="4" height="7" fill="var(--navy-deep)"/></svg>
        <span>+555-010-2040</span>
      </li>
      <li class="contact__item">
        <svg class="contact__icon" viewBox="0 0 14 14" aria-label="Fax"><rect x="3" y="1" width="8" height="5" fill="var(--accent-orange)"/><rect x="0.5" y="5" width="13" height="7" rx="1" fill="var(--accent-orange)"/><rect x="3" y="8" width="8" height="2" fill="var(--navy-deep)"/></svg>
        <span>+555-010-2041</span>
      </li>
      <li class="contact__item">
        <svg class="contact__icon" viewBox="0 0 14 14" aria-label="Email"><rect x="0.5" y="3" width="13" height="9" fill="var(--accent-orange)"/><path d="M0.5,3 L7,8 L13.5,3" fill="none" stroke="var(--navy-deep)" stroke-width="1.2"/></svg>
        <span>info@velnastack.com</span>
      </li>
      <li class="contact__item">
        <svg class="contact__icon" viewBox="0 0 14 14" aria-label="Website"><circle cx="7" cy="7" r="6.3" fill="var(--accent-orange)"/><g fill="none" stroke="var(--navy-deep)" stroke-width="0.9"><ellipse cx="7" cy="7" rx="2.6" ry="6.3"/><line x1="0.7" y1="7" x2="13.3" y2="7"/></g></svg>
        <span>www.velnastack.com</span>
      </li>
    </ul>

    <address class="address">
      Suite xxx, 214 Harbour Lane<br>
      Northgate, Victoria 3100
    </address>
  </section>

</main>
</body>
</html>
```